zSTRIDA Membership Flyer

zSTRIDA is a shoe store selling brand name sneakers like Vorn Keltro Brisk Talvan and etc. We need a flyer to promote our membership program. On this flyer we need to emphasize that people who sign up can get 20% off their entire first purchase(certain items are excluded), which is limited time offer.
The flyer is 5.5"X4.25", two sided.
On the back side, there need to be a section where customer can fill up their name, phone number and email to join the membership.
our website is www.zstridashop.example
Member benefits can also be found on the website and should be on the flyer.

Industry/Entity Type

Shoe Store

```html
<!DOCTYPE html>
<html lang="en">
<head>
<meta charset="utf-8">
<title>zSTRIDA Membership Flyer</title>
<link rel="stylesheet" href="https://fonts.googleapis.com/css2?family=Archivo:wght@700;800&display=swap">
<style>
  :root {
    --frame-green: #4dff00;
    --accent-orange: #ff7a1a;
    --ink: #000000;
    --paper: #ffffff;
  }
  html, body {
    margin: 0;
    padding: 0;
    width: 1200px;
    height: 927px;
    overflow: hidden;
    background: var(--paper);
  }
  .flyer {
    position: relative;
    box-sizing: border-box;
    width: 1200px;
    height: 927px;
    border: 14px solid var(--frame-green);
    background: var(--paper);
    font-family: "Archivo", Arial, sans-serif;
    font-weight: 700;
    color: var(--ink);
    overflow: hidden;
  }
  .headline {
    position: absolute;
    top: 34px;
    left: 0;
    right: 0;
    margin: 0;
    text-align: center;
    font-size: 57px;
    line-height: 54px;
    font-weight: 700;
    letter-spacing: 1px;
    word-spacing: 16px;
  }
  .headline .offer { color: var(--accent-orange); }
  .headline .mark {
    font-size: 30px;
    vertical-align: 22px;
    margin-left: 2px;
  }
  .signup-field {
    position: absolute;
    left: 41px;
    width: 1090px;
    border-bottom: 3px solid var(--ink);
    font-size: 23px;
    line-height: 26px;
    font-weight: 800;
    word-spacing: 6px;
    padding-bottom: 1px;
  }
  .field-name { top: 225px; }
  .field-phone { top: 334px; }
  .field-email { top: 441px; }
  .store-name {
    position: absolute;
    top: 560px;
    left: 0;
    right: 0;
    margin: 0;
    text-align: center;
    font-size: 132px;
    line-height: 150px;
    font-weight: 800;
    letter-spacing: 4px;
    color: var(--ink);
  }
  .offer-note {
    position: absolute;
    top: 728px;
    left: 0;
    right: 0;
    margin: 0;
    text-align: center;
    font-size: 26px;
    line-height: 34px;
    font-weight: 700;
    word-spacing: 4px;
  }
  .offer-note .limited { color: var(--accent-orange); }
  .website-note {
    position: absolute;
    top: 770px;
    left: 0;
    right: 0;
    margin: 0;
    text-align: center;
    font-size: 22px;
    line-height: 30px;
    font-weight: 700;
    word-spacing: 3px;
  }
  .fine-print {
    position: absolute;
    left: 41px;
    top: 844px;
    margin: 0;
    font-size: 16px;
    font-weight: 700;
    word-spacing: 4px;
  }
</style>
</head>
<body>
  <main class="flyer">
    <h1 class="headline">
      SIGN UP NOW AND EARN<br>
      <span class="offer">20% OFF</span> YOUR FIRST PURCHASE<span class="mark">*</span>
    </h1>

    <div class="signup-field field-name">Name:</div>
    <div class="signup-field field-phone">Phone Number:</div>
    <div class="signup-field field-email">Email Address:</div>

    <p class="store-name">zSTRIDA</p>
    <p class="offer-note"><span class="limited">LIMITED TIME OFFER</span> on your entire first purchase</p>
    <p class="website-note">See all member benefits at www.zstridashop.example</p>

    <p class="fine-print">*Some exclusions apply</p>
  </main>
</body>
</html>
```